Home Design company focused on remodel and enhancement of kitchens and bathroorms

I already have a logo designed by ArtHarbor, I now need a design for my business cards.
The company is in the remodeling and enhancement industry for homes, focusing on kitchens and bathrooms, however, we can remodel or enhance every room in a home, an office space, etc.

The company's name is VELMOR HOME DESIGN, LLC

We'll focus on clients in the Rio Grande Valley, Texas. Primarily McAllen, Edinburg, Pharr, Mission, Brownsville and South Padre Island.

The design on the business card should transmit reliability, professionalism anda bit of upscale design.

The logo is in black and white, and would like to keep it that way.

The information that needs to be printed in the business cards is:
Company's name: Velmor Home Design
Company's Logo (attached)
My name: Noel Bramwit
Address, phone and email:
2715 N Parkline Road, Ste 348
Harlow Springs, TX 70100
(555) 010 0187
nbramwit@velmordesign.example
Website: velmordesign.example

```html
<!DOCTYPE html>
<html lang="en">
<head>
<meta charset="utf-8">
<title>Velmor Home Design — Business Card</title>
<link rel="stylesheet" href="https://fonts.googleapis.com/css2?family=Montserrat:wght@400;600;700&display=swap">
<style>
  :root {
    --bg: #9a9a9a;
    --card-front: #ffffff;
    --card-back: #2f2f2f;
    --ink: #242424;
    --ink-soft: #3a3a3a;
    --back-mark: #1c1c1c;
  }
  * { box-sizing: border-box; margin: 0; padding: 0; }
  html, body { width: 1200px; height: 1059px; overflow: hidden; }
  body {
    background: var(--bg);
    font-family: "Montserrat", sans-serif;
    position: relative;
  }
  .card {
    position: absolute;
    width: 688px;
    height: 392px;
    border-radius: 24px;
    overflow: hidden;
  }
  .card--front { left: 256px; top: 89px; background: var(--card-front); color: var(--ink); }
  .card--back { left: 253px; top: 569px; width: 694px; height: 394px; background: var(--card-back); }

  .brand {
    position: absolute;
    display: flex;
    align-items: center;
  }
  .brand__square { background: var(--ink); flex: none; }
  .brand__name {
    font-weight: 400;
    text-transform: uppercase;
    line-height: 1.05;
    white-space: nowrap;
  }
  .card--front .brand { left: 38px; top: 56px; gap: 22px; }
  .card--front .brand__square { width: 60px; height: 60px; }
  .card--front .brand__name { font-size: 21px; letter-spacing: 5px; color: var(--ink); }

  .card--back .brand { left: 128px; top: 150px; gap: 34px; }
  .card--back .brand__square { width: 90px; height: 90px; background: var(--back-mark); }
  .card--back .brand__name { font-size: 33px; letter-spacing: 8px; font-weight: 600; color: var(--back-mark); }

  .person {
    position: absolute;
    right: 37px;
    top: 172px;
    text-align: right;
  }
  .person__name { font-weight: 700; font-size: 25px; letter-spacing: 0.5px; line-height: 1.1; }
  .person__title { font-size: 16px; color: var(--ink-soft); margin-top: 2px; }
  .edge-tab {
    position: absolute;
    right: 0; top: 177px;
    width: 18px; height: 38px;
    background: var(--ink);
  }

  .contact {
    position: absolute;
    left: 38px;
    top: 228px;
    font-size: 17px;
    color: var(--ink-soft);
    letter-spacing: 0.3px;
    white-space: nowrap;
  }
  .contact__address { line-height: 22px; margin-bottom: 9px; }
  .contact__row { display: flex; align-items: center; gap: 5px; height: 24px; }
  .contact__icon { width: 12px; height: 12px; flex: none; fill: var(--ink); }
  .contact__icon--outline { fill: none; stroke: var(--ink); stroke-width: 2; }
</style>
</head>
<body>

<section class="card card--front" aria-label="Card front">
  <div class="brand">
    <span class="brand__square"></span>
    <p class="brand__name">Velmor<br>Home<br>Design</p>
  </div>

  <div class="person">
    <p class="person__name">NOEL BRAMWIT</p>
    <p class="person__title">CEO/Founder</p>
  </div>
  <span class="edge-tab"></span>

  <div class="contact">
    <p class="contact__address">2715 N Parkline Road<br>Ste 348 Harlow Springs, TX 70100</p>
    <p class="contact__row">
      <svg class="contact__icon" viewBox="0 0 24 24"><path d="M6.6 10.8a15.1 15.1 0 0 0 6.6 6.6l2.2-2.2c.3-.3.7-.4 1-.2 1.1.4 2.3.6 3.6.6.6 0 1 .4 1 1V20c0 .6-.4 1-1 1A17 17 0 0 1 3 4c0-.6.4-1 1-1h3.5c.6 0 1 .4 1 1 0 1.3.2 2.5.6 3.6.1.3 0 .7-.2 1z"/></svg>
      (555) 010 0187
    </p>
    <p class="contact__row">
      <svg class="contact__icon" viewBox="0 0 24 24"><path d="M2 5h20v2l-10 6L2 7z M2 9l10 6 10-6v10H2z"/></svg>
      nbramwit@velmordesign.example
    </p>
    <p class="contact__row">
      <svg class="contact__icon contact__icon--outline" viewBox="0 0 24 24"><circle cx="12" cy="12" r="10"/><path d="M2 12h20M12 2c3 3 3 17 0 20M12 2c-3 3-3 17 0 20"/></svg>
      www.velmordesign.example
    </p>
  </div>
</section>

<section class="card card--back" aria-label="Card back">
  <div class="brand">
    <span class="brand__square"></span>
    <p class="brand__name">Velmor<br>Home<br>Design</p>
  </div>
</section>

</body>
</html>
```